Web Design Project

I need designs (PSD only - no programming) for several pages of a new website helping train operators to manage key information about their traindrivers.
The main feature of this website is the management of personnel records (create, edit, search, delete). Another key aspect is the management of user privileges. Since this is a new website we also need a user friendly frontpage, pricing information and how it works sections.
This can be broken down into 9 pages for which we need designs (PSDs).
1. Home
2. Driver record
3. How it works
4. Pricing
5. User administration
6. Help
7. Record list view
8. Login
9. Registration
Navigation (not logged in) are: Home | How it works | Pricing | Customers | About us | Contact
Navigation (logged in) are: Overview | Administration | Manage records | Billing | Help | Contact
Footer: Customer logos | Awards | Terms & Conditions | Privacy
To provide the best support for you to come up with a strong design proposal I will provide DAILY feedback to all participants. We have also created concept mockups (attached) and example pages (below) for each section to give you a clear sense of what we look for.
The core concepts for a successful bid are that the website is EASY to understand, INTUITIVE to navigate, and SIMPLE to use. Most of our users lack technical background and are looking for tool to simplify their work.
The strongest participants (winner and close contenders) will have the opportunity to additional commissioned work on additional sections not included in this brief.
Example Pages (by section)
1. http://www.brovendale.example/site-keepers/
1. http://www.qvt.example/
1. http://www.mondaph.example/
1. http://www.gorvanquest.example/
2. http://www.snapveld.example/profile_edit.gne
3. https://www.tarn.example/how-it-works/
3. http://www.bulkvue.example/learn
4. http://www.pactheron.example/crm/editions-pricing.jsp
4. http://www.brovendale.example/site-keepers/prices
6. https://support.talvora.example/en-gb/
6. http://help.dealmeadow.example/contact_us
8. https://www.careweave.example/uas/login
8. https://www.dealmeadow.example/login
8. http://www.askhollow.example/login/index
For form designs we like Verindo, Bidnook, Snapveld, CareWeave, Chatterly and the concepts presented by Tomas Kerrigan in his classic Layout Craft Shaping the Input Boxes.
For additional guidance see mockups attached!
Target Market(s)
Security, human resources and admin support employees for train operators.
Industry/Entity Type
Learn
Requirements
Should not have
- Home page should not have
Social media icons (chatterly, chirpla, CareWeave, RSS feed)
Contact forms
Read more links
Old trains

```html
<!DOCTYPE html>
<html lang="en">
<head>
<meta charset="utf-8">
<title>TrackLedger – Prices</title>
<link href="https://fonts.googleapis.com/css2?family=Montserrat:wght@400;500;600;700&display=swap" rel="stylesheet">
<style>
:root{
  --ink:#3d3d3d;
  --navy:#1f3d6b;
  --nav:#1d3e6e;
  --sky:#5bc3de;
  --orange:#f3861f;
  --grey:#8d8d8d;
  --rule:#dcdcdc;
  --plat:#4e2370;
  --gold:#f0b01c;
  --silver:#7b716f;
  --bronze:#f06a22;
}
*{box-sizing:border-box;margin:0;padding:0}
html,body{width:1200px;height:1010px;overflow:hidden;background:#fff}
body{font-family:"Montserrat",sans-serif;color:var(--ink);position:relative}
.site-header{position:absolute;left:0;top:0;width:1200px;height:114px;background:linear-gradient(#fff 0,#fff 40px,#e6e6e6 106px);border-bottom:8px solid var(--orange)}
.util-links{position:absolute;top:14px;left:898px;display:flex;gap:19px;font-size:12px;color:#555}
.brand{position:absolute;left:124px;top:44px;font-size:37px;font-weight:600;color:#3aa9c9;letter-spacing:-.5px;text-decoration:none}
.main-nav{position:absolute;top:50px;left:416px;display:flex;gap:0}
.main-nav a{display:block;height:34px;line-height:34px;padding:0 15px;margin-right:7px;font-size:17px;font-weight:600;color:var(--nav);text-decoration:none;border-radius:5px}
.main-nav a.active{background:linear-gradient(#7dd2e9,#3fb2d3);color:#fff}
.page-title{position:absolute;left:120px;top:142px;font-size:22px;font-weight:700;color:var(--navy)}
.title-rule{position:absolute;left:120px;top:176px;width:958px;height:1px;background:var(--rule)}
.plan{position:absolute;text-align:center;font-size:14.5px;line-height:24px}
.plan-head{height:79px;color:#fff;padding-top:14px}
.plan-head .tag{font-size:17px;font-weight:400;opacity:.9}
.plan-head .name{font-size:24px;font-weight:700;line-height:30px;text-shadow:0 1px 2px rgba(0,0,0,.3)}
.plan-body{padding-top:22px}
.plan-body .b{font-weight:600;color:#222}
.plan-body .gap{height:24px}
.order{position:absolute;left:50%;transform:translateX(-50%);width:165px;height:40px;line-height:40px;border-radius:3px;font-size:16px;font-weight:700;color:#fff;text-decoration:none;box-shadow:0 1px 2px rgba(0,0,0,.25)}
.platinum{left:124px;top:214px;width:237px;height:390px;background:linear-gradient(#f4f3f8,#d6d4e4)}
.platinum .plan-head{background:var(--plat)}
.platinum .order{top:326px;background:linear-gradient(#6a3a92,#4a1f6c)}
.gold{left:366px;top:214px;width:232px;height:390px;background:linear-gradient(#fffaf0,#fde1b3)}
.gold .plan-head{background:var(--gold)}
.gold .order{top:326px;background:linear-gradient(#fbd12c,#f0b01c)}
.silver{left:599px;top:199px;width:247px;height:409px;background:linear-gradient(#f7f6f6,#dcdada);border:4px solid #fff;box-shadow:0 2px 10px rgba(0,0,0,.3);z-index:2}
.silver .plan-head{background:var(--silver)}
.silver .order{top:334px;background:linear-gradient(#6a6a6a,#2f2f2f)}
.bronze{left:846px;top:214px;width:232px;height:390px;background:linear-gradient(#fff2ea,#fdd2bb)}
.bronze .plan-head{background:linear-gradient(#f48a2c,var(--bronze))}
.bronze .plan-body{padding-top:14px}
.bronze .order{top:326px;background:linear-gradient(#f9902f,#ef6a1e)}
.intro{position:absolute;left:155px;top:682px;width:890px;text-align:center;font-size:16.5px;line-height:24px;color:var(--grey)}
.partners-title{position:absolute;left:121px;top:818px;font-size:22px;font-weight:700;color:#a3a3a3}
.partners-rule{position:absolute;left:121px;top:852px;width:957px;height:1px;background:var(--rule)}
.scroll-up{position:absolute;left:566px;top:824px}
.partner-row{position:absolute;left:126px;top:876px;width:960px;display:flex;justify-content:space-between}
.partner{width:44px;height:44px;background:#c9c7c7}
.partner.round{border-radius:50%}
.partner.soft{border-radius:8px}
.footer-rule{position:absolute;left:121px;top:948px;width:957px;height:1px;background:var(--rule)}
.copyright{position:absolute;left:121px;top:967px;font-size:12px;color:#888}
.copyright a{color:#2d4f9e;text-decoration:none}
.footer-nav{position:absolute;right:122px;top:967px;font-size:12px;color:#888}
.footer-nav a{color:#888;text-decoration:none}
</style>
</head>
<body>
<header class="site-header">
  <nav class="util-links"><span>Sign Up</span><span>Login</span><span>Language</span></nav>
  <a class="brand" href="#">TrackLedger</a>
  <nav class="main-nav">
    <a href="#">Home</a><a href="#">How it Works</a><a class="active" href="#">Prices</a><a href="#">Our Customers</a><a href="#">About Us</a><a href="#">Contact</a>
  </nav>
</header>

<h1 class="page-title">Price</h1>
<div class="title-rule"></div>

<section class="plan platinum">
  <div class="plan-head"><div class="tag">Ultimate</div><div class="name">PLATINUM</div></div>
  <div class="plan-body">
    <div class="b">200 EUR / month</div><div>(or just 1999 EUR/year)</div><div class="gap"></div>
    <div>20,000 stored pages</div><div>20,000 page modifications</div><div>200,000 pageviews /</div><div class="b">Auto change notification</div>
  </div>
  <a class="order" href="#">ORDER NOW!</a>
</section>

<section class="plan gold">
  <div class="plan-head"><div class="tag">More Pageviews</div><div class="name">GOLD</div></div>
  <div class="plan-body">
    <div class="b">50 EUR / month</div><div>(or just 499 EUR/year)</div>
    <div>5,000 stored pages</div><div>5,000 page modifications</div><div>50,000 pageviews /month</div><div class="gap"></div>
    <div>Auto change notification</div><div>1-click XLIFF upload</div>
  </div>
  <a class="order" href="#">ORDER NOW!</a>
</section>

<section class="plan silver">
  <div class="plan-head"><div class="tag">Most Popular</div><div class="name">SILVER</div></div>
  <div class="plan-body">
    <div class="b">200 EUR / month</div><div>(or just 1999 EUR/year)</div><div class="gap"></div>
    <div>20,000 stored pages</div><div>20,000 page modifications</div><div>200,000 pageviews /</div><div class="b">Auto change notification</div>
  </div>
  <a class="order" href="#">ORDER NOW!</a>
</section>

<section class="plan bronze">
  <div class="plan-head"><div class="tag">Basic Plan</div><div class="name">BRONZE</div></div>
  <div class="plan-body">
    <div class="b">50 EUR / month</div><div>(or just 499 EUR/year)</div>
    <div>5,000 stored pages</div><div>5,000 page modifications</div><div>50,000 pageviews /month</div><div class="gap"></div>
    <div>Auto change notification</div><div>1-click XLIFF upload</div>
  </div>
  <a class="order" href="#">ORDER NOW!</a>
</section>

<p class="intro">Lorem Ipsum is simply dummy text of the printing and typesetting industry. Lorem Ipsum has been the industry's standard dummy text ever since the 1500s, when an unknown printer took a galley of type and scrambled it to make a type specimen book. It has survived not only five centuries.</p>

<h2 class="partners-title">Our Partners:</h2>
<div class="partners-rule"></div>
<svg class="scroll-up" width="96" height="30" viewBox="0 0 96 30" aria-hidden="true">
  <path d="M0 30 A48 30 0 0 1 96 30 Z" fill="#efefef"/>
  <path d="M41 16 L48 10 L55 16" fill="none" stroke="#999" stroke-width="2.5"/>
</svg>
<div class="partner-row">
  <div class="partner soft"></div><div class="partner round"></div><div class="partner soft"></div><div class="partner round"></div>
  <div class="partner round"></div><div class="partner round"></div><div class="partner soft"></div><div class="partner soft"></div>
  <div class="partner soft"></div><div class="partner soft"></div><div class="partner round"></div>
</div>

<div class="footer-rule"></div>
<footer>
  <p class="copyright">© 2012 Trackledger. All Rights reserved. <a href="#">Terms &amp; Conditions</a></p>
  <nav class="footer-nav"><a href="#">Home</a> &nbsp;-&nbsp; <a href="#">How it works</a> &nbsp;-&nbsp; <a href="#">Prices</a> &nbsp;-&nbsp; <a href="#">Our Customers</a> &nbsp;-&nbsp; <a href="#">About us</a> &nbsp;-&nbsp; <a href="#">Contact</a></nav>
</footer>
</body>
</html>
```